Flyer für Hausärzte
Aufgabenstellung
Der Flyer soll das Format DIN 105 lang haben und später bei druckwelle.de gedruckt werden. Entsprechende Vorlagen sind bei druckwelle.de vorhanden. Der Flyer wird in der Mitte 1x gefalzt und beidseitige bedruckt. (Es gibt also eine Außenseite, eine Doppel Innenseiten und eine Rückseite)
Der Flyer soll Neupatienten sowie BEstandspatienten ansprechen und über die Ärzte und die Leistungen informieren. Siehe www.praxis-lindenbogen.de
Die Fotos auf der Homepage können verwendet werden, entsprechende Lizenzen für die Nutzung liegen vor. An besseren Ideen bin ich natürlich auch interessiert :-)
Datenübergabe in Adobe Illustrator (.ai) oder Adobe InDesign (.indd)
Vielen Dank und beste Grüße

```html
<!DOCTYPE html>
<html lang="de">
<head>
<meta charset="utf-8">
<title>Hausärzte – Flyer DIN lang</title>
<link rel="stylesheet" href="https://fonts.googleapis.com/css2?family=Source+Serif+4:opsz,wght@8..60,400;8..60,600;8..60,700&family=Inter:wght@400;500&display=swap">
<style>
  :root {
    --page-bg: #e9eaea;
    --ink: #2a2d33;
    --ink-soft: #4a4e55;
    --cover-title: #f3f1f2;
    --sheet: #ffffff;
    --cell-grey: #d6d7d7;
    --cell-mint: #cbd8d7;
    --cell-sand: #dfe0cc;
    --cell-blue: #a9c0d4;
    --thumb-bg: #eef0f1;
    --serif: "Source Serif 4", Georgia, serif;
    --sans: "Inter", Arial, sans-serif;
  }
  * { box-sizing: border-box; margin: 0; padding: 0; }
  html, body { width: 1200px; height: 900px; overflow: hidden; }
  body { background: var(--page-bg); position: relative; }

  .flyer {
    position: absolute; left: 270px; top: 100px;
    width: 660px; height: 700px;
    display: flex;
  }
  .panel { width: 330px; height: 700px; position: relative; overflow: hidden; }

  /* Cover panel */
  .cover-photo {
    position: absolute; inset: 0;
    background: linear-gradient(180deg,
      #8fa0b3 0%, #a9aabd 25%, #c3b5c4 42%, #e2c6b9 52%,
      #d9c2a9 56%, #6f7782 60%, #5b6470 75%, #3f454d 100%);
  }
  .cover-kicker {
    position: absolute; left: 28px; top: 58px;
    font-family: var(--serif); font-weight: 400; font-size: 29px;
    color: var(--cover-title); letter-spacing: 0.2px;
  }
  .cover-headline {
    position: absolute; left: 28px; top: 148px;
    font-family: var(--serif); font-weight: 400; font-size: 40px;
    line-height: 1.15; color: var(--ink); letter-spacing: -0.3px;
  }

  /* Team panel */
  .team { background: var(--sheet); display: flex; flex-direction: column; }
  .team-header { height: 122px; padding: 42px 20px 0; }
  .team-title {
    font-family: var(--serif); font-weight: 400; font-size: 20px;
    line-height: 1.2; color: var(--ink);
  }
  .team-grid {
    height: 428px;
    display: grid; grid-template-columns: 1fr 1fr; grid-template-rows: repeat(4, 1fr);
  }
  .card { display: flex; gap: 10px; padding: 38px 10px 0 18px; }
  .card--grey { background: var(--cell-grey); }
  .card--mint { background: var(--cell-mint); }
  .card--sand { background: var(--cell-sand); }
  .card--blue { background: var(--cell-blue); }
  .card-thumb { width: 42px; height: 42px; flex: none; background: linear-gradient(160deg, #e9ebec, #c5ccd3); }
  .card-thumb--object { background: linear-gradient(160deg, #f4f5f5, #dfe3e6); }
  .card-name {
    font-family: var(--serif); font-weight: 600; font-size: 13.5px;
    color: var(--ink); margin-bottom: 6px;
  }
  .card-lines { list-style: none; font-family: var(--sans); font-size: 7px; line-height: 1.45; color: var(--ink-soft); }

  .team-footer { flex: 1; padding: 38px 20px 0; font-family: var(--sans); color: var(--ink); }
  .footer-format { font-size: 13px; font-weight: 500; margin-bottom: 4px; }
  .footer-note { font-size: 11px; line-height: 1.4; }
</style>
</head>
<body>
  <main class="flyer">
    <section class="panel cover">
      <div class="cover-photo" role="img" aria-label="Foto des Praxisgebäudes in der Abenddämmerung mit beleuchteten Fenstern"></div>
      <p class="cover-kicker">Hausärzte</p>
      <h1 class="cover-headline">Your health<br>in good hands</h1>
    </section>

    <section class="panel team">
      <header class="team-header">
        <h2 class="team-title">Unser Praxisteam<br>im Überblick</h2>
      </header>

      <div class="team-grid">
        <article class="card card--grey">
          <div class="card-thumb" role="img" aria-label="Porträt der Ärztin"></div>
          <div><h3 class="card-name">Kolbe</h3>
            <ul class="card-lines"><li>Fachärztin Allgemein</li><li>Innere Medizin</li><li>Hausbesuche Mo–Fr</li></ul></div>
        </article>
        <article class="card card--mint">
          <div class="card-thumb" role="img" aria-label="Porträt des Arztes"></div>
          <div><h3 class="card-name">Korte</h3>
            <ul class="card-lines"><li>Facharzt Allgemein</li><li>Reisemedizin</li><li>Impfberatung</li></ul></div>
        </article>
        <article class="card card--grey">
          <div class="card-thumb card-thumb--object" role="img" aria-label="Illustration einer Spritze"></div>
          <div><h3 class="card-name">Labor</h3>
            <ul class="card-lines"><li>Blutentnahme täglich</li><li>Ergebnisse zeitnah</li><li>Urin und EKG</li></ul></div>
        </article>
        <article class="card card--mint">
          <div class="card-thumb card-thumb--object" role="img" aria-label="Illustration eines Stethoskops"></div>
          <div><h3 class="card-name">Vorsorge</h3>
            <ul class="card-lines"><li>Check-up ab 35</li><li>Krebsvorsorge jährlich</li><li>Hautscreening</li></ul></div>
        </article>
        <article class="card card--sand">
          <div class="card-thumb" role="img" aria-label="Porträt des Arztes"></div>
          <div><h3 class="card-name">Kahlen</h3>
            <ul class="card-lines"><li>Facharzt Innere</li><li>Diabetologie</li><li>Schulungen</li></ul></div>
        </article>
        <article class="card card--blue">
          <div class="card-thumb" role="img" aria-label="Porträt der Ärztin"></div>
          <div><h3 class="card-name">Casper</h3>
            <ul class="card-lines"><li>Fachärztin Allgemein</li><li>Psychosomatik</li><li>Akupunktur</li></ul></div>
        </article>
        <article class="card card--sand">
          <div class="card-thumb" role="img" aria-label="Porträt des Arztes mit Stethoskop"></div>
          <div><h3 class="card-name">Seeck</h3>
            <ul class="card-lines"><li>Weiterbildungsassistent</li><li>Sportmedizin</li><li>Ultraschall</li></ul></div>
        </article>
        <article class="card card--blue">
          <div class="card-thumb" role="img" aria-label="Porträt der Praxismanagerin"></div>
          <div><h3 class="card-name">Stein</h3>
            <ul class="card-lines"><li>Praxismanagement</li><li>Termine Rezepte</li><li>Überweisungen</li></ul></div>
        </article>
      </div>

      <footer class="team-footer">
        <p class="footer-format">DIN Lang 105</p>
        <p class="footer-note">Persönliche Betreuung<br>wohnortnah und mit Zeit für Ihr Anliegen.</p>
      </footer>
    </section>
  </main>
</body>
</html>
```